Option Sheet

We need a one page option sheet with a left to right reading of the five options. It should be a one sheet, multiple colors and definitive separations between options This is used in a sales consultation. Backround or colors not in option need to have the follow RGB value (5 red, 20 green, 63 blue)

We added a smaller text file, please change that point

Target Market(s)

Divorce

Industry/Entity Type

Legal

Requirements
Must have
• 1) All five options left to right
• 2)language included in sheet

```html
<!DOCTYPE html>
<html lang="en">
<head>
<meta charset="utf-8">
<title>Five Options – Divorce</title>
<link href="https://fonts.googleapis.com/css2?family=Cinzel:wght@700;900&family=Lora:wght@700&family=Marcellus&display=swap" rel="stylesheet">
<style>
  :root {
    --navy: rgb(5, 20, 63);
    --ink: #ffffff;
    --rose: #cf727c;
    --tan: #bfa273;
    --gold: #e6b263;
    --sage: #97ba6e;
    --sky: #a4cfef;
  }
  * { margin: 0; padding: 0; box-sizing: border-box; }
  html, body { width: 848px; height: 1200px; overflow: hidden; background: var(--navy); }
  .sheet { position: relative; width: 848px; height: 1200px; background: var(--navy); color: var(--ink); }
  .sheet-title { position: absolute; top: 16px; left: 0; width: 848px; text-align: center; font-family: "Cinzel", serif; font-weight: 700; line-height: 1; }
  .sheet-title .kicker { display: block; font-size: 31px; letter-spacing: 5px; }
  .sheet-title .topic { display: block; font-size: 35px; letter-spacing: 2px; margin-top: 5px; }

  .option { position: absolute; left: 0; width: 848px; height: 160px; }
  .option svg { position: absolute; top: -12px; left: 0; width: 848px; height: 172px; overflow: visible; }
  .option--do-nothing { top: 156px; --accent: var(--rose); }
  .option--counseling { top: 363px; --accent: var(--tan); }
  .option--diy { top: 574px; --accent: var(--gold); }
  .option--limited { top: 783px; --accent: var(--sage); }
  .option--hire { top: 989px; left: -3px; --accent: var(--sky); }

  .badge-number, .badge-name { position: absolute; left: 22px; width: 169px; text-align: center; font-family: "Cinzel", serif; font-weight: 900; color: var(--ink); text-shadow: 1px 2px 2px rgba(0,0,0,.45); line-height: 1; }
  .badge-number { font-size: 46px; transform: translateY(-50%); }
  .badge-name { font-size: 18px; line-height: 17px; transform: translateY(-50%); }
  .badge-name.small { font-size: 14px; }

  .label { position: absolute; right: 523px; font-family: "Lora", serif; font-weight: 700; font-size: 17px; line-height: 1; transform: translateY(-50%); white-space: nowrap; }
  .points { position: absolute; left: 346px; list-style: none; font-family: "Marcellus", serif; font-size: 15px; line-height: 16.5px; white-space: nowrap; }
  .points li { position: relative; padding-left: 11px; }
  .points li::before { content: "•"; position: absolute; left: 0; font-size: 11px; }
  .points.tight { letter-spacing: -0.5px; line-height: 15px; }
  .points.tighter { letter-spacing: -0.9px; line-height: 16.5px; font-size: 14.5px; }
</style>
</head>
<body>
<main class="sheet">
  <h1 class="sheet-title"><span class="kicker">FIVE OPTIONS</span><span class="topic">DIVORCE</span></h1>

  <!-- shared frame drawn per option -->
  <section class="option option--do-nothing">
    <svg viewBox="0 -12 848 172" aria-hidden="true">
      <g fill="var(--accent)" stroke="var(--accent)">
        <line x1="64" y1="0" x2="556" y2="0" stroke-width="2.5"/>
        <line x1="64" y1="147" x2="818" y2="147" stroke-width="2.5"/>
        <polygon points="558,-10 569,-10 575,0 569,10 558,10 552,0" stroke="none"/>
        <polygon points="64,1 150,1 191,74 150,148 64,148 22,74" stroke="none"/>
        <polygon points="790,96 821,96 835,121 821,147 790,147 776,121" stroke="none"/>
      </g>
      <rect x="796" y="111" width="20" height="20" rx="2" fill="none" stroke="#fff" stroke-width="2"/>
    </svg>
    <div class="badge-number" style="top:40px">01</div>
    <div class="badge-name" style="top:74px">DO NOTHING</div>
    <div class="label" style="top:39px">Advantages:</div>
    <ul class="points" style="top:22px"><li>Stay married</li><li>No life Changes</li></ul>
    <div class="label" style="top:95px">Disadvantages:</div>
    <ul class="points" style="top:73px"><li>Remain unhappy, depressed, anxious</li><li>Money and assets may disappear</li><li>What is going to change?</li></ul>
  </section>

  <section class="option option--counseling">
    <svg viewBox="0 -12 848 172" aria-hidden="true">
      <g fill="var(--accent)" stroke="var(--accent)">
        <line x1="64" y1="0" x2="556" y2="0" stroke-width="2.5"/>
        <line x1="64" y1="147" x2="818" y2="147" stroke-width="2.5"/>
        <polygon points="558,-10 569,-10 575,0 569,10 558,10 552,0" stroke="none"/>
        <polygon points="64,1 150,1 191,74 150,148 64,148 22,74" stroke="none"/>
        <polygon points="790,96 821,96 835,121 821,147 790,147 776,121" stroke="none"/>
      </g>
      <rect x="796" y="111" width="20" height="20" rx="2" fill="none" stroke="#fff" stroke-width="2"/>
    </svg>
    <div class="badge-number" style="top:44px">02</div>
    <div class="badge-name" style="top:86px">GO TO<br>COUNSELING</div>
    <div class="label" style="top:39px">Advantages:</div>
    <ul class="points" style="top:21px"><li>Reconcile marriage</li><li>Help make a better life</li></ul>
    <div class="label" style="top:94px">Disadvantages:</div>
    <ul class="points tight" style="top:74px"><li>Past issues are highlighted and may drudge up old wounds</li><li>It may just clarify the reasons you need to separate and/or<br>divorce</li><li>Both parties must be invested and willing to participate</li></ul>
  </section>

  <section class="option option--diy">
    <svg viewBox="0 -12 848 172" aria-hidden="true">
      <g fill="var(--accent)" stroke="var(--accent)">
        <line x1="64" y1="0" x2="556" y2="0" stroke-width="2.5"/>
        <line x1="64" y1="147" x2="818" y2="147" stroke-width="2.5"/>
        <polygon points="558,-10 569,-10 575,0 569,10 558,10 552,0" stroke="none"/>
        <polygon points="64,1 150,1 191,74 150,148 64,148 22,74" stroke="none"/>
        <polygon points="790,96 821,96 835,121 821,147 790,147 776,121" stroke="none"/>
      </g>
      <rect x="796" y="111" width="20" height="20" rx="2" fill="none" stroke="#fff" stroke-width="2"/>
    </svg>
    <div class="badge-number" style="top:46px">03</div>
    <div class="badge-name" style="top:87px">DO IT<br>YOURSELF</div>
    <div class="label" style="top:34px">Advantages:</div>
    <ul class="points" style="top:16px"><li>No attorney fees</li><li>You are your on attorney</li></ul>
    <div class="label" style="top:92px">Disadvantages:</div>
    <ul class="points tight" style="top:63px"><li>People often find that what is “fair,” may in fact, not be truly fair</li><li>Often times, people do not know the risks</li><li>Complicated legal system within intrigue rules</li><li>Unsure how to complete the necessary paperwork and<br>meet the deadlines</li></ul>
  </section>

  <section class="option option--limited">
    <svg viewBox="0 -12 848 172" aria-hidden="true">
      <g fill="var(--accent)" stroke="var(--accent)">
        <line x1="64" y1="0" x2="556" y2="0" stroke-width="2.5"/>
        <line x1="64" y1="147" x2="818" y2="147" stroke-width="2.5"/>
        <polygon points="558,-10 569,-10 575,0 569,10 558,10 552,0" stroke="none"/>
        <polygon points="64,1 150,1 191,74 150,148 64,148 22,74" stroke="none"/>
        <polygon points="790,96 821,96 835,121 821,147 790,147 776,121" stroke="none"/>
      </g>
      <rect x="796" y="111" width="20" height="20" rx="2" fill="none" stroke="#fff" stroke-width="2"/>
    </svg>
    <div class="badge-number" style="top:39px">04</div>
    <div class="badge-name" style="top:72px">LIMITED</div>
    <div class="badge-name small" style="top:89px">REPRESENTATION</div>
    <div class="label" style="top:36px">Advantages:</div>
    <ul class="points" style="top:18px"><li>Balance between going alone and our limited involvement<br>in the case</li></ul>
    <div class="label" style="top:95px">Disadvantages:</div>
    <ul class="points tighter" style="top:60px"><li>Our terms may not benefit from our legal knowledge</li><li>The legal consequences of your legal documents will not be explained<br>to you so that you can formulate a plan for handling the rest of your case.</li><li>Your spouse or other parties may cause your legal fees to increase<br>significantly without action on your part</li></ul>
  </section>

  <section class="option option--hire">
    <svg viewBox="0 -12 848 172" aria-hidden="true">
      <g fill="var(--accent)" stroke="var(--accent)">
        <line x1="64" y1="0" x2="556" y2="0" stroke-width="2.5"/>
        <line x1="64" y1="147" x2="818" y2="147" stroke-width="2.5"/>
        <polygon points="558,-10 569,-10 575,0 569,10 558,10 552,0" stroke="none"/>
        <polygon points="64,1 150,1 191,74 150,148 64,148 22,74" stroke="none"/>
        <polygon points="790,96 821,96 835,121 821,147 790,147 776,121" stroke="none"/>
      </g>
      <rect x="796" y="111" width="20" height="20" rx="2" fill="none" stroke="#fff" stroke-width="2"/>
    </svg>
    <div class="badge-number" style="top:42px">05</div>
    <div class="badge-name" style="top:83px">HIRE US</div>
    <div class="label" style="top:56px">Advantages:</div>
    <ul class="points tight" style="top:38px"><li>Gain the full benefits of our experience</li><li>Have a team of Family Law focus attorneys</li><li>Often saves you or makes you money in the long run</li><li>Save you time, energy and stress</li></ul>
    <div class="label" style="top:122px">Disadvantages:</div>
    <ul class="points" style="top:114px"><li>Initial cost</li></ul>
  </section>
</main>
</body>
</html>
```